BHSM Business Card Design Project

We are a Wedding Film company in Charleston, SC In need of a unique business card. Our website is www.brightharborstudiomedia.com. Check us out to get an idea of who we are and what we do. The design should be upscale but not pretentious. Modern but not cheesy. I will most likely have our cards printed by Zell on the Plume design. I'm also liking the raised designs for our logo. The Wedding Films in our logo on our site is blue so feel free to manipulate our logo for your designs as well.

Industry/Entity Type

Business

Requirements
Must have
• This is the info I want on the card:

Derek Halloway
Storyteller

Brightharbor Studio Media
www.brightharborstudiomedia.com

843.627.4150
derek@brightharborstudiomedia.com

```html
<!DOCTYPE html>
<html lang="en">
<head>
<meta charset="utf-8">
<title>Brightharbor Studio Media – Business Card</title>
<link rel="stylesheet" href="https://fonts.googleapis.com/css2?family=Source+Sans+3:wght@300;400;600;700&display=swap">
<style>
  :root {
    --backdrop: #e9e4dc;
    --card: #0c0b0a;
    --gold: #b99a5c;
    --gold-light: #d9c47c;
    --rule: #6f5f3d;
  }
  * { box-sizing: border-box; margin: 0; padding: 0; }
  html, body {
    width: 1200px;
    height: 665px;
    overflow: hidden;
    background: var(--backdrop);
    font-family: "Source Sans 3", "Myriad Pro", sans-serif;
  }
  .stage {
    position: relative;
    width: 1200px;
    height: 665px;
    display: flex;
    align-items: center;
    justify-content: center;
    gap: 50px;
  }
  .card {
    position: relative;
    width: 530px;
    height: 303px;
    background: var(--card);
    box-shadow: 0 8px 20px rgba(0,0,0,0.25);
    color: var(--gold);
  }
  .brand {
    position: absolute;
    left: 0;
    right: 0;
    display: flex;
    align-items: center;
    justify-content: center;
    gap: 12px;
    font-weight: 300;
    color: var(--gold);
    letter-spacing: 0.5px;
  }
  .brand__mark {
    border-radius: 50%;
    background: var(--gold);
    flex: none;
  }
  .card--front .brand { top: 70px; font-size: 34px; }
  .card--front .brand__mark { width: 30px; height: 30px; }
  .rule {
    position: absolute;
    height: 1px;
    background: var(--rule);
  }
  .card--front .rule--top { left: 24px; right: 24px; top: 172px; }
  .card--front .rule--bottom { left: 24px; right: 24px; top: 268px; }
  .contact {
    position: absolute;
    left: 0;
    right: 0;
    text-align: center;
    font-size: 12px;
    color: var(--gold-light);
  }
  .contact__person { top: 184px; font-size: 15px; }
  .contact__name { font-weight: 700; }
  .contact__title { font-weight: 400; font-size: 12px; }
  .contact__lines { top: 212px; display: flex; justify-content: center; gap: 28px; }
  .contact__web { top: 234px; }
  .card--back .brand { top: 104px; font-size: 38px; flex-direction: column; gap: 16px; }
  .card--back .brand__mark { width: 44px; height: 44px; }
  .card--back .rule--top { left: 24px; right: 24px; top: 236px; }
  .card--back .site {
    position: absolute;
    left: 0; right: 0;
    top: 256px;
    text-align: center;
    font-size: 13px;
    color: var(--gold-light);
  }
  .site strong { font-weight: 700; }
</style>
</head>
<body>
<main class="stage">
  <section class="card card--front" aria-label="Card front">
    <div class="brand"><span class="brand__mark"></span><span class="brand__name">Brightharbor Studio Media</span></div>
    <div class="rule rule--top"></div>
    <p class="contact contact__person"><span class="contact__name">Derek Halloway /</span> <span class="contact__title">Storyteller</span></p>
    <p class="contact contact__lines"><span>P : 843.627.4150</span><span>E : derek@brightharborstudiomedia.com</span></p>
    <p class="contact contact__web">W : www.brightharborstudiomedia.com</p>
    <div class="rule rule--bottom"></div>
  </section>
  <section class="card card--back" aria-label="Card back">
    <div class="brand"><span class="brand__mark"></span><span class="brand__name">Brightharbor Studio Media</span></div>
    <div class="rule rule--top"></div>
    <p class="site">www.<strong>brightharborstudiomedia</strong>.com</p>
  </section>
</main>
</body>
</html>
```